Vexorun.co is a multi-sport platform that connects players, clubs, coaches, and organizers in one ecosystem.

Core value:
- Players can instantly find or create games across sports (padel, pickleball, tennis, soccer, etc.)
- Clubs can manage players, classes, staff, and tournaments in one place
- Coaches and organizers can create events and earn money directly through the platform

Key differentiator:
Vexorun is not just for finding games — it is a revenue engine for clubs and sports communities.

Main features to highlight:
- Find and join games instantly
- Create games without coordination friction
- Club management (players, classes, payments)
- Coaches offering lessons and programs
- Tournaments and events between clubs
- Fill empty court time with automated or quick-created events

Business model:
- Free to join
- Platform takes a small fee on transactions (events, classes, subscriptions)

Tagline:
“Let the Games Begin & Pick Your Challenge”

Tone:
Modern, premium, community-driven, and action-oriented.
Focus on simplicity, energy, and real usage scenarios.

Target Market(s)

multi-sport platform that connects players, clubs, coaches, and organizers in one ecosystem.

Industry/Entity Type

Sport

Coding

Coded - Design and coding required

Number of Pages Required

3 page

Requirements
Must have
• Build you the exact Webflow structure (class-by-class export)
Nice to have
• Html y css

```html
<!DOCTYPE html>
<html lang="en">
<head>
<meta charset="utf-8">
<title>Vexorun — Let the Games Begin &amp; Pick Your Challenge</title>
<link href="https://fonts.googleapis.com/css2?family=Anybody:wdth,wght@150,800;150,900&family=DM+Sans:wght@400;500;600&display=swap" rel="stylesheet">
<style>
:root{
  --bg:#0c0f0c;
  --bg-alt:#101510;
  --bg-deep:#0a0d0a;
  --card:#161c16;
  --card-2:#1b211b;
  --line:#263026;
  --green:#4caf50;
  --green-bright:#62d04f;
  --green-soft:#1f3a1f;
  --text:#f2f5f2;
  --muted:#9aa39a;
  --dim:#6f786f;
  --display:'Anybody',sans-serif;
  --body:'DM Sans',sans-serif;
}
*{box-sizing:border-box;margin:0;padding:0}
html,body{width:1200px;height:3729px;overflow:hidden;background:var(--bg);color:var(--text);font-family:var(--body)}
.page{position:relative;width:1200px;height:3729px}
.abs{position:absolute}
.brand{display:flex;align-items:center;gap:7px;font-family:var(--body);font-weight:600;font-size:14px;color:var(--text)}
.brand-dot{width:18px;height:18px;border-radius:50%;background:var(--green)}
.btn{display:flex;align-items:center;justify-content:center;border-radius:6px;font-weight:600;font-size:14px}
.btn-solid{background:var(--green);color:#fff}
.btn-ghost{border:1px solid #4a564a;color:var(--text)}
.eyebrow{font-size:10px;letter-spacing:1.2px;text-transform:uppercase;color:var(--green-bright);font-weight:500}
.display{font-family:var(--display);font-weight:900;font-stretch:150%;font-variation-settings:"wdth" 150;letter-spacing:-.5px;line-height:1.08}
.center{text-align:center;left:0;width:1200px}

/* nav */
.nav{top:0;left:0;width:1200px;height:64px;background:#0b0e0b;border-bottom:1px solid #1a201a}
.nav .brand{position:absolute;left:41px;top:21px}
.nav .btn{position:absolute;left:1009px;top:17px;width:151px;height:33px;font-size:12px}

/* hero */
.hero{top:64px;left:0;width:1200px;height:751px;background:radial-gradient(ellipse 420px 260px at 880px 120px,#1c3a1c 0%,rgba(12,15,12,0) 100%),var(--bg)}
.pill{display:inline-flex;align-items:center;gap:7px;height:26px;padding:0 13px;border:1px solid #2f4a2f;border-radius:14px;background:#142014;font-size:10px;letter-spacing:.6px;color:var(--green-bright)}
.pill i{width:5px;height:5px;border-radius:50%;background:var(--green-bright)}
.hero-title{left:100px;top:88px;font-size:54px;line-height:60px;letter-spacing:-1px}
.hero-title .accent{color:var(--green-bright)}
.hero-lead{left:100px;top:467px;width:380px;font-size:15px;line-height:24px;color:var(--muted)}
.hero-lead b{color:var(--text);font-weight:500}
.flags{left:100px;top:630px;width:460px;font-size:9px;color:var(--dim);display:flex;flex-wrap:wrap;align-items:center;gap:14px 14px}
.flag{width:14px;height:9px;border-radius:1px;background:#3a443a}
.phone{left:745px;top:231px;width:235px;height:258px;border-radius:24px;border:2px solid #2a352a;background:#111611;padding:18px 14px}
.phone .brand{font-size:9px;gap:4px}
.phone .brand-dot{width:11px;height:11px}
.play-card{margin-top:14px;height:65px;border-radius:8px;background:linear-gradient(135deg,#2f6a2f,#1c3a1c);border:1px solid #3d7a3d;padding:12px}
.play-card small{display:block;font-size:7px;color:#bcd6bc}
.play-card b{display:flex;align-items:center;gap:7px;margin-top:6px;font-size:14px;font-weight:600}
.play-card b i{width:20px;height:20px;border-radius:50%;background:#7bd36b;position:relative}
.play-card b i:after{content:"";position:absolute;left:8px;top:6px;border-left:6px solid #1c3a1c;border-top:4px solid transparent;border-bottom:4px solid transparent}
.match-card{margin-top:11px;border-radius:8px;background:#1a1f1a;border:1px solid #263026;padding:10px 10px 8px}
.match-card .eyebrow{font-size:7px}
.player{display:flex;gap:8px;align-items:center;margin-top:9px}
.player i{width:18px;height:18px;border-radius:50%;background:#2a5a2a;border:1px solid #4a8a4a}
.player b{display:block;font-size:9px;font-weight:600}
.player span{font-size:8px;color:var(--muted)}

/* stats */
.stats{top:815px;left:0;width:1200px;height:136px;background:var(--bg-alt);border-top:1px solid #1c241c;border-bottom:1px solid #1c241c;display:flex;justify-content:center;align-items:center}
.stat{width:230px;text-align:center;border-right:1px solid #253025}
.stat:last-child{border-right:0}
.stat b{display:block;font-family:var(--display);font-weight:900;font-stretch:150%;font-variation-settings:"wdth" 150;font-size:26px;line-height:32px}
.stat b em{font-style:normal;color:var(--green-bright)}
.stat span{font-size:11px;color:var(--muted)}

/* features */
.features{top:951px;left:0;width:1200px;height:617px;background:var(--bg)}
.sec-title{font-size:36px}
.sec-lead{font-size:14px;line-height:23px;color:var(--muted)}
.card-row{left:140px;width:920px;display:flex;gap:21px}
.card{flex:1;background:var(--card);border:1px solid var(--line);border-radius:8px;padding:24px}
.icon{width:34px;height:34px;border-radius:6px;background:var(--green-soft);border:1px solid #2f4a2f;display:flex;align-items:center;justify-content:center}
.card h3{margin-top:20px;font-size:16px;font-weight:600}
.card p{margin-top:12px;font-size:12px;line-height:20px;color:var(--muted)}
.card ul{list-style:none;margin-top:12px}
.card li{font-size:11px;color:var(--muted);line-height:26px}
.card li:before{content:"•";color:var(--green-bright);margin-right:7px}

/* who */
.who{top:1568px;left:0;width:1200px;height:543px;background:var(--bg-deep)}
.who .card{height:207px;background:var(--card-2)}
.who .card h3{margin-top:14px}
.who .icon{background:none;border:0;width:auto;justify-content:flex-start}

/* expansion */
.expansion{top:2111px;left:0;width:1200px;height:462px;background:linear-gradient(180deg,#131a13,#0c0f0c)}
.checks{left:140px;top:263px;list-style:none}
.checks li{display:flex;gap:13px;font-size:14px;line-height:21px;margin-bottom:14px;width:420px}
.checks li i{flex:none;width:17px;height:17px;border-radius:50%;background:var(--green);display:flex;align-items:center;justify-content:center;margin-top:2px}
.cities{left:634px;top:138px;width:426px;height:187px;background:#111711;border:1px solid var(--line);border-radius:10px;padding:28px 26px}
.city-grid{display:grid;grid-template-columns:repeat(4,1fr);gap:11px 0;margin-top:18px}
.city{font-size:10px;color:var(--muted);display:flex;align-items:center;gap:6px}
.city:before{content:"";width:6px;height:6px;border-radius:50%;background:var(--green)}
.legend{margin-top:16px;font-size:10px;color:var(--dim);display:flex;gap:10px;align-items:center}
.legend i{display:inline-block;width:10px;height:10px;border-radius:50%;background:var(--green);margin-right:4px;vertical-align:-1px}
.legend i.soon{background:#4a544a;width:8px;height:8px}

/* waitlist */
.waitlist{top:2573px;left:0;width:1200px;height:1051px;background:linear-gradient(180deg,#0c0f0c,#121812)}
.waitlist .pill{font-size:11px}
.form{left:316px;top:367px;width:567px;height:581px;border:1px solid var(--line);border-radius:12px;background:#111611;padding:0 31px}
.field{position:absolute;left:31px;width:505px}
.field label,.join-label{display:block;font-size:11px;font-weight:500;margin-bottom:8px}
.input{height:36px;border:1px solid #2e382e;border-radius:5px;background:#1d231d;padding:0 14px;font-size:12px;color:#858e85;display:flex;align-items:center;justify-content:space-between}
.row{display:flex;gap:13px}
.row>div{flex:1}
.join-label{font-size:9px;letter-spacing:.8px;color:var(--muted);font-weight:400}
.toggle{flex:1;height:51px;border:1px solid #2e382e;border-radius:6px;display:flex;align-items:center;gap:9px;padding:0 16px;font-size:12px;color:var(--muted)}
.toggle.on{border-color:var(--green);background:#1a2a1a;color:var(--green-bright)}
.toggle i{width:11px;height:11px;border-radius:3px;background:currentColor;opacity:.7}
.submit{height:44px;gap:8px;font-size:13px}
.note{font-size:12px;color:var(--muted);text-align:center}

/* footer */
.footer{top:3624px;left:0;width:1200px;height:105px;background:#0a0c0a;border-top:1px solid #1a201a}
.footer .brand{position:absolute;left:41px;top:44px;font-size:12px}
.footer .copy{position:absolute;left:0;width:1200px;text-align:center;top:45px;font-size:11px;color:var(--muted)}
.footer nav{position:absolute;right:41px;top:45px;display:flex;gap:26px;font-size:11px;color:var(--muted)}
</style>
</head>
<body>
<div class="page">

  <header class="abs nav">
    <div class="brand"><span class="brand-dot"></span>vexorun</div>
    <a class="btn btn-solid">Get Early Access</a>
  </header>

  <section class="abs hero">
    <div class="abs" style="left:100px;top:37px"><span class="pill"><i></i>NOW LAUNCHING GLOBALLY</span></div>
    <h1 class="abs display hero-title">The global<br>network<br>for<br><span class="accent">players,<br>matches,</span><br>and clubs</h1>
    <p class="abs hero-lead"><b>Let the Games Begin &amp; Pick Your Challenge.</b> Find games, book coaches, join events — anywhere in the world.</p>
    <a class="abs btn btn-solid" style="left:100px;top:547px;width:155px;height:46px">Join as Player</a>
    <a class="abs btn btn-ghost" style="left:268px;top:547px;width:145px;height:46px">Join as Club</a>
    <div class="abs flags">
      <span>Built for Pickleball &amp; Padel — expanding to all sports:</span>
      <span class="flag"></span><span class="flag"></span><span class="flag"></span><span class="flag"></span><span class="flag"></span><span class="flag"></span><span class="flag"></span>
      <span class="flag"></span><span class="flag"></span><span class="flag"></span>
    </div>
    <div class="abs phone">
      <div class="brand"><span class="brand-dot"></span>vexorun</div>
      <div class="play-card">
        <small>Today · Harbourline Park</small>
        <b><i></i>Play Now</b>
      </div>
      <div class="match-card">
        <div class="eyebrow">Find matches</div>
        <div class="player"><i></i><div><b>Tomás Ibarra</b><span>Level 4.0 · 2 km away</span></div></div>
        <div class="player"><i></i><div><b>Lena Marchetti</b><span>Level 3.5 · 1.4 km away</span></div></div>
      </div>
    </div>
  </section>

  <section class="abs stats">
    <div class="stat"><b>12<em>+</em></b><span>Countries active</span></div>
    <div class="stat"><b>50<em>k+</em></b><span>Players registered</span></div>
    <div class="stat"><b>2<em>k+</em></b><span>Clubs onboarded</span></div>
    <div class="stat"><b>∞</b><span>Sports coming soon</span></div>
  </section>

  <section class="abs features">
    <p class="abs center eyebrow" style="top:90px">Everything in one place</p>
    <h2 class="abs center display sec-title" style="top:112px">Your sport. Fully connected.</h2>
    <p class="abs center sec-lead" style="top:170px">No more scattered Chatterly groups or half-empty courts.<br>Not just finding games — a revenue engine for clubs.</p>
    <div class="abs card-row" style="top:269px;height:264px">
      <div class="card">
        <div class="icon"><svg width="16" height="16"><circle cx="8" cy="8" r="7" fill="#b5e04a"/></svg></div>
        <h3>Find Matches</h3>
        <p>Find or create games at your exact skill level, instantly or in advance.</p>
        <ul><li>Play instantly or schedule games</li><li>Match with players at your level</li><li>Skill-based smart matching</li></ul>
      </div>
      <div class="card">
        <div class="icon"><svg width="16" height="16"><path d="M3 2h10v4a5 5 0 0 1-10 0z" fill="#e2b53a"/><rect x="6" y="11" width="4" height="4" fill="#e2b53a"/></svg></div>
        <h3>Join Events &amp; Leagues</h3>
        <p>Discover tournaments, open events, and club leagues near you.</p>
        <ul><li>Browse upcoming events</li><li>Register with one tap</li><li>Track your results &amp; ranking</li></ul>
      </div>
      <div class="card">
        <div class="icon"><svg width="16" height="16"><circle cx="8" cy="8" r="7" fill="#3a7ad0"/><path d="M4 6h4v4H5z" fill="#5fbf4f"/></svg></div>
        <h3>Global Community</h3>
        <p>Build your sporting network across cities and countries.</p>
        <ul><li>Find courts anywhere you travel</li><li>Book lessons with local coaches</li><li>12 languages and counting</li></ul>
      </div>
    </div>
  </section>

  <section class="abs who">
    <p class="abs center eyebrow" style="top:88px">Who it's for</p>
    <h2 class="abs center display sec-title" style="top:112px;line-height:43px">Built for how people actually<br>play sports</h2>
    <div class="abs card-row" style="top:252px">
      <div class="card">
        <div class="icon"><svg width="22" height="22"><circle cx="11" cy="11" r="9" fill="#e2b53a"/></svg></div>
        <h3>For Players</h3>
        <p>Find games instantly. Meet players at your level. Never miss a match near you again.</p>
      </div>
      <div class="card">
        <div class="icon"><svg width="22" height="22"><rect x="2" y="6" width="18" height="12" rx="3" fill="#c9574a"/></svg></div>
        <h3>For Clubs</h3>
        <p>Fill empty courts, manage players, classes and payments, and grow revenue.</p>
      </div>
      <div class="card">
        <div class="icon"><svg width="22" height="22"><rect x="4" y="2" width="14" height="18" rx="2" fill="#d8c7a2"/><rect x="8" y="1" width="6" height="3" fill="#8a7a5a"/></svg></div>
        <h3>For Coaches &amp; Organizers</h3>
        <p>Run lessons, leagues, and tournaments — and earn directly, no spreadsheets.</p>
      </div>
    </div>
  </section>

  <section class="abs expansion">
    <p class="abs eyebrow" style="left:140px;top:90px">Expansion</p>
    <h2 class="abs display sec-title" style="left:140px;top:112px;line-height:43px">Launching<br>city by city<br>worldwide</h2>
    <ul class="abs checks">
      <li><i><svg width="9" height="9"><path d="M1 5l2.5 2.5L8 2" stroke="#fff" stroke-width="1.5" fill="none"/></svg></i>Building the first global sports network</li>
      <li><i><svg width="9" height="9"><path d="M1 5l2.5 2.5L8 2" stroke="#fff" stroke-width="1.5" fill="none"/></svg></i>Starting with Pickleball &amp; Padel — the fastest-growing racket sports worldwide</li>
      <li><i><svg width="9" height="9"><path d="M1 5l2.5 2.5L8 2" stroke="#fff" stroke-width="1.5" fill="none"/></svg></i>Expanding to all sports in 2025 and beyond</li>
    </ul>
    <div class="abs cities">
      <p class="eyebrow">Active &amp; upcoming cities</p>
      <div class="city-grid">
        <span class="city">London</span><span class="city">Madrid</span><span class="city">Paris</span><span class="city">Miami</span>
        <span class="city">São Paulo</span><span class="city">Dubai</span><span class="city">Sydney</span><span class="city">Tokyo</span>
        <span class="city">Toronto</span><span class="city">NYC</span><span class="city">Berlin</span><span class="city">Mumbai</span>
      </div>
      <div class="legend"><span><i></i>Live</span><span><i class="soon"></i>Coming soon — register your city</span></div>
    </div>
  </section>

  <section class="abs waitlist">
    <div class="abs center" style="top:103px"><span class="pill">⚡&nbsp; EARLY ACCESS</span></div>
    <h2 class="abs center display sec-title" style="top:150px;line-height:43px">Be first on the<br>court</h2>
    <p class="abs sec-lead" style="left:320px;width:560px;top:256px;text-align:center;line-height:24px">Join the waitlist and get exclusive early access — before your city officially launches. Free to join; founding members get priority placement, premium features, and a direct line to our team.</p>
    <form class="abs form">
      <div class="field row" style="top:39px">
        <div><label>First name</label><div class="input">Alex</div></div>
        <div><label>Last name</label><div class="input">Rivera</div></div>
      </div>
      <div class="field" style="top:113px"><label>Email address</label><div class="input">alex@email.com</div></div>
      <div class="field" style="top:187px"><label>Your city</label><div class="input">London, Madrid, Miami...</div></div>
      <div class="field" style="top:262px"><label>Primary sport</label><div class="input" style="color:#cfd5cf">Select your sport<svg width="10" height="6"><path d="M1 1l4 4 4-4" stroke="#9aa39a" fill="none"/></svg></div></div>
      <div class="field" style="top:340px">
        <span class="join-label">I WANT TO JOIN AS</span>
        <div class="row"><div class="toggle on"><i></i>Player</div><div class="toggle"><i></i>Club / Coach / Organizer</div></div>
      </div>
      <div class="field" style="top:431px"><a class="btn btn-solid submit">Reserve my spot <svg width="12" height="10"><path d="M0 5h10M6 1l4 4-4 4" stroke="#fff" stroke-width="1.5" fill="none"/></svg></a></div>
      <p class="field note" style="top:491px">🔒 No spam. No credit card. Just early access.</p>
    </form>
  </section>

  <footer class="abs footer">
    <div class="brand"><span class="brand-dot"></span>vexorun</div>
    <p class="copy">© 2025 Vexorun. Let the Games Begin &amp; Pick Your Challenge.</p>
    <nav><a>Privacy</a><a>Terms</a><a>Contact</a></nav>
  </footer>

</div>
</body>
</html>
```